Venture Capital Investment Firm

We are looking to overhaul our existing website (substantially), with only using the same logos (which we can provide).
We are an investment firm that focuses on making loans to late stage technology companies. Our site should ultimately look like other venture capital firms, and look modern and fresh. We have an existing website www.brenvoltfund.com which this will be replacing, although we will be using a lot of the existing written content, and potentially the numbers of pages we will need, we are not wed to anything else. Please feel free to shoot any questions at any time and thank you in advance for your help!
Websites we like as examples:
https://www.tarnwickbay.com/
https://www.morrowlanefinance.com/
Target Market(s)
Potential investors who will invest in our firm, as well as potentially companies that are looking to borrow money from us.
Coding
Colors
Look and feel

```html
<!DOCTYPE html>
<html lang="en">
<head>
<meta charset="utf-8">
<title>Brenvolt Fund — Partners for Growth</title>
<link href="https://fonts.googleapis.com/css2?family=Roboto:wght@300;400;500;700&display=swap" rel="stylesheet">
<style>
:root{
  --orange:#f7a10a;
  --blue:#1d9de4;
  --blue-text:#1a8fdc;
  --white:#ffffff;
  --body-grey:#555555;
  --footer-bg:#262626;
  --footer-text:#7b7b7b;
  --field:#bdbdbd;
}
*{margin:0;padding:0;box-sizing:border-box}
html,body{width:1200px;height:2441px;overflow:hidden}
body{font-family:'Roboto',sans-serif;background:var(--white);position:relative}
.abs{position:absolute}

/* hero */
.hero{position:absolute;left:0;top:0;width:1200px;height:673px;overflow:hidden}
.hero-photo{position:absolute;inset:0;background:
  radial-gradient(ellipse at 50% 25%,#8ea4b8 0%,rgba(142,164,184,0) 45%),
  linear-gradient(180deg,#3f4a57 0%,#566b80 40%,#4f7fa8 75%,#5b8fb8 100%)}
.brand{position:absolute;color:var(--white);font-weight:400;display:flex;align-items:center;letter-spacing:.5px}
.brand .dot{display:inline-block;border-radius:50%;background:var(--white);margin-right:8px}
.nav-brand{left:90px;top:45px;font-size:22px}
.nav-brand .dot{width:14px;height:14px}
.nav a{position:absolute;top:49px;color:var(--white);font-size:15px;font-weight:500;text-decoration:none}
.nav .active::after{content:"";position:absolute;left:-8px;right:-8px;top:29px;height:1px;background:var(--white)}
.nav .investors{left:1014px;top:44px;width:100px;height:30px;background:var(--orange);border-radius:3px;display:flex;align-items:center;justify-content:center}
.hero-brand{left:130px;top:212px;font-size:40px}
.hero-brand .dot{width:28px;height:28px;margin-right:12px}
.hero-title{left:130px;top:294px;font-size:66px;font-weight:500;color:var(--white);letter-spacing:.5px}
.hero-sub{left:130px;top:377px;width:560px;font-size:19px;line-height:23px;color:var(--white);font-weight:400}
.hero-sub b{font-weight:700}
.btn{position:absolute;background:var(--orange);color:var(--white);border-radius:26px;display:flex;align-items:center;justify-content:center;box-shadow:0 3px 6px rgba(0,0,0,.18)}
.hero-btn{left:130px;top:468px;width:206px;height:52px;font-size:12px;font-weight:700;box-shadow:none}

/* about */
.about{position:absolute;left:0;top:673px;width:1200px;height:609px;background:var(--white);border:1px solid #cfcfcf}
.section-title{position:absolute;left:93px;font-size:40px;font-weight:300;letter-spacing:1px}
.section-rule{position:absolute;left:95px;width:57px;height:1px}
.about .section-title{top:84px;color:var(--blue-text)}
.about .section-rule{top:146px;background:var(--blue-text)}
.about-lead{left:99px;top:177px;font-size:18.5px;font-weight:700;color:var(--orange)}
.about-h{left:99px;font-size:18.5px;font-weight:500;color:var(--blue-text);width:1010px;line-height:23px}
.about-p{left:99px;font-size:16px;color:var(--body-grey);width:1030px;line-height:20px}
.btn-team{left:93px;width:175px;height:47px;font-size:13px;letter-spacing:.5px}

/* experience */
.experience{position:absolute;left:0;top:1282px;width:1200px;height:701px;background:var(--blue);color:var(--white)}
.experience .section-title{top:44px}
.experience .section-rule{top:111px;background:var(--white)}
.stat{position:absolute;top:152px}
.stat-over{font-size:18px}
.stat-value{font-size:64px;font-weight:300;margin-top:3px;line-height:72px;letter-spacing:1px}
.stat-rule{width:59px;height:1px;background:var(--white);margin-top:2px}
.stat-label{font-size:12px;margin-top:14px}
.exp-p{left:95px;width:1030px;font-size:15.5px;line-height:20.7px}

/* footer */
.footer{position:absolute;left:0;top:1983px;width:1200px;height:458px;background:var(--footer-bg)}
.foot-links a{position:absolute;left:130px;color:var(--white);font-size:13px;text-decoration:none}
.foot-about{left:396px;top:96px;width:412px;text-align:center;color:var(--footer-text);font-size:14.5px;line-height:18.2px;font-weight:300}
.login{position:absolute;left:885px;color:var(--white);font-size:12px;font-weight:500}
.field{position:absolute;left:885px;width:221px;height:29px;background:var(--field);border:1px solid #e0e0e0}
.submit{position:absolute;left:885px;top:264px;width:110px;height:27px;background:var(--orange);color:var(--white);font-size:12px;font-weight:700;display:flex;align-items:center;justify-content:center}
.foot-rule{left:66px;top:323px;width:1069px;height:1px;background:#4a4a4a}
.foot-brand{left:0;width:1200px;top:345px;justify-content:center;font-size:22px}
.foot-brand .dot{width:14px;height:14px}
.foot-meta{left:0;width:1200px;text-align:center;color:var(--footer-text);font-size:11px}
</style>
</head>
<body>

<header class="hero">
  <div class="hero-photo" role="img" aria-label="Upward view of glass skyscrapers against a grey-blue sky"></div>
  <div class="brand nav-brand"><span class="dot"></span>Brenvolt</div>
  <nav class="nav">
    <a class="active" style="left:482px">Home</a>
    <a style="left:571px">Strategy</a>
    <a style="left:661px">About Us</a>
    <a style="left:750px">Team</a>
    <a style="left:839px">News</a>
    <a style="left:928px">Contact</a>
    <a class="investors">Investors</a>
  </nav>
  <div class="brand hero-brand"><span class="dot"></span>Brenvolt</div>
  <h1 class="abs hero-title">PARTNERS FOR GROWTH</h1>
  <p class="abs hero-sub">WE ARE A GLOBAL STRUCTURED CREDIT INVESTMENT FIRM FOCUSED ON THE <b>HEALTHCARE AND TECHNOLOGY INDUSTRIES</b></p>
  <div class="btn hero-btn">About our strategy</div>
</header>

<section class="about">
  <h2 class="section-title">About us</h2>
  <div class="section-rule"></div>
  <p class="abs about-lead">BRENVOLT FUND STARTED WITH A BIG IDEA:&nbsp; FINANCE PROVEN INNOVATION WITH A DIFFERENT APPROACH</p>
  <h3 class="abs about-h" style="top:220px">Brenvolt Fund is a private investment firm unique in its dual focus on life science and technology credit opportunities.</h3>
  <p class="abs about-p" style="top:249px">Our ambidextrous approach to investing reflects a broad recognition and appreciation for the critical role intellectual property plays in the successful commercialization of products.&nbsp; We apply our extensive industry expertise to assess the revenue visibility created by these assets and offer a range of creative financing solutions.</p>
  <h3 class="abs about-h" style="top:348px">A pioneer in providing life science structured credit beginning in 2004, the Brenvolt Fund team was the first to introduce flexible structured credit to the technology sector in 2014</h3>
  <p class="abs about-p" style="top:398px">Our team was also early to recognize the potential of "non-core" assets beyond drug royalties, acquiring over $300M of branded generics offering predictable cash flows from large pharmaceutical firms and partnering with entrepreneurial teams to successfully manage these brands.</p>
  <div class="btn btn-team" style="top:499px">MEET THE TEAM</div>
</section>

<section class="experience">
  <h2 class="section-title">Our experience</h2>
  <div class="section-rule"></div>
  <div class="stat" style="left:148px">
    <div class="stat-over">OVER</div>
    <div class="stat-value">$1.2B</div>
    <div class="stat-rule"></div>
    <div class="stat-label">INVESTED BY OUR PARTNERS</div>
  </div>
  <div class="stat" style="left:469px">
    <div class="stat-over">OVER</div>
    <div class="stat-value">40</div>
    <div class="stat-rule"></div>
    <div class="stat-label">LIFE SCIENCE AND ECHNOLOGY INVESTMENTS</div>
  </div>
  <div class="stat" style="left:791px">
    <div class="stat-over">OVER A</div>
    <div class="stat-value">DECADE</div>
    <div class="stat-rule"></div>
    <div class="stat-label">INNOVATING FINANCING STRUCTURES</div>
  </div>
  <p class="abs exp-p" style="top:372px">We bring over 40 years of collective experience to our investments, including over $1.2B invested within structured credit, milestones and royalties, and the acquisition of legacy assets from some of the world's largest and most well respected pharmaceutical companies.&nbsp; In addition, members of the Brenvolt Fund team have played senior roles in executing over $75B of M&amp;A, equity, and debt financings in the life science and technology sectors.</p>
  <p class="abs exp-p" style="top:454px">Along the way we've built strong relationships and friendships with entrepreneurial management teams, investors, and executives who acquire and commercialize innovative products and technologies.&nbsp; These relationships offer Brenvolt Fund unique insight into the industries, companies, and products where we invest.</p>
  <div class="btn btn-team" style="top:576px">MEET THE TEAM</div>
</section>

<footer class="footer">
  <nav class="foot-links">
    <a style="top:107px">Home</a>
    <a style="top:140px">Strategy</a>
    <a style="top:173px">About us</a>
    <a style="top:206px">Team</a>
    <a style="top:239px">News</a>
    <a style="top:272px">Contact</a>
  </nav>
  <p class="abs foot-about">Brenvolt Fund is a private investment firm unique in its dual focus on life science<br>and technology credit opportunities.&nbsp; Our ambidextrous approach to<br>investing reflects a broad recognition and appreciation for the critical role<br>intellectual property plays in the successful commercialization of products.<br>We apply our extensive industry expertise to assess the revenue visibility<br>created by these assets and offer a range of creative financing solutions.</p>
  <div class="login" style="top:99px">Investor login</div>
  <div class="login" style="top:132px">Username</div>
  <div class="field" style="top:148px"></div>
  <div class="login" style="top:197px">Password</div>
  <div class="field" style="top:210px"></div>
  <div class="submit">Submit</div>
  <div class="abs foot-rule"></div>
  <div class="brand foot-brand"><span class="dot"></span>Brenvolt</div>
  <div class="abs foot-meta" style="top:397px">BRENVOLT FUND, SAN FRANCISCO</div>
  <div class="abs foot-meta" style="top:426px">© 2015 Brenvolt Investment Partners LLC.&nbsp; All Rights Reserved.&nbsp;&nbsp;&nbsp;&nbsp;&nbsp; Legal Disclaimer</div>
</footer>

</body>
</html>
```